Biz Card Design TPVC

New business card for a new company.
Logo was completed by a designer on ArtFlock and looking to continue requesting additional services.
Company Name: Tidal Prime Voltage Collective
Although this company is starting in Canada, we will be moving towards a global presence within the next 6 months.
Key elements to this business are as follows.
Energy Procurement
Energy Reduction Services
Demand Side Consulting
Energy Efficiency Consulting
Saving Clients Money
Helping Them Go "Green"
Managing Their Energy Requirements
Basically the goal for our company is to find the best procurement solution for our clients and reduce their energy consumption. This reduces their expenses and the amount of greenhouse gas they produce on a daily basis.
I have been in the energy footprint for the last 20 years and know that most companies are looking to "do whatever is necessary to get them to sign on the dotted line". I would prefer to walk away from a client that I can't help than to put them into a situation that they will regret for years to come. This is where the "TIDAL" part of the company name comes from.
The following is a catch phrase that encompasses what we do.
"Reducing your carbon footprint & energy bill at the same time!"
The back of the card needs to have this statement along with some sort of illustration. The back is a playground for creative ideas.
The front of the card needs the following.
Logo.
First & Last Name (Gus Marwick)
Title (Energy Warrior)
Phone Number (555) 314-2768
Fax Number (555) 862-4091
Email Address gus@tidalprimevoltage.example
Address 47 Orchard Lane Toronto Ontario K4P 2Z7
I want it to be a card that is remembered when any of my staff give it to a customer. It HAS to stand out.
Target Market(s)
Business Owners, Decision Makers, 30 to 65+
Industry/Entity Type
Business
Look and feel
Each slider illustrates characteristics of the customer's brand and the style your logo design should communicate.

```html
<!DOCTYPE html>
<html lang="en">
<head>
<meta charset="utf-8">
<title>Tidal Prime Voltage Collective – Business Card</title>
<link rel="stylesheet" href="https://fonts.googleapis.com/css2?family=Montserrat:ital,wght@0,400;0,600;0,700;1,400&family=EB+Garamond:ital@1&display=swap">
<style>
  :root {
    --page: #ffffff;
    --card-edge: #b5b5b5;
    --brand-blue: #3a6fb6;
    --brand-green: #3dae4a;
    --back-green: #27b14a;
    --back-light: #6fcd7e;
    --ink-label: #222222;
    --white: #ffffff;
  }
  * { margin: 0; padding: 0; box-sizing: border-box; }
  html, body {
    width: 1200px;
    height: 900px;
    overflow: hidden;
    background: var(--page);
  }
  .sheet {
    position: relative;
    width: 1200px;
    height: 900px;
    font-family: "Montserrat", Arial, sans-serif;
  }
  .card {
    position: absolute;
    width: 414px;
    height: 238px;
  }
  .card-front {
    left: 190px;
    top: 166px;
    border: 1.5px solid var(--card-edge);
    background: var(--white);
    text-align: center;
  }
  .brand-mark {
    display: block;
    width: 34px;
    height: 34px;
    margin: 25px auto 0;
    border-radius: 50%;
    background: var(--brand-green);
  }
  .brand-name {
    margin-top: 12px;
    font-size: 18px;
    line-height: 22px;
    font-weight: 700;
    letter-spacing: -0.3px;
    color: var(--brand-blue);
  }
  .holder-name {
    margin-top: 28px;
    font-size: 14px;
    line-height: 17px;
    font-weight: 700;
    letter-spacing: 1px;
    color: var(--brand-blue);
    text-transform: uppercase;
  }
  .holder-title {
    margin-top: 2px;
    font-size: 11px;
    line-height: 14px;
    font-weight: 600;
    color: var(--brand-green);
  }
  .contact {
    margin-top: 6px;
    font-size: 12.5px;
    line-height: 18px;
    color: var(--brand-blue);
  }
  .contact-lines { color: var(--brand-green); }
  .contact-sep { margin: 0 6px; }
  .card-back {
    left: 708px;
    top: 538px;
    height: 236px;
    overflow: hidden;
    background: var(--back-green);
  }
  .back-art {
    position: absolute;
    left: 0;
    top: 0;
    width: 300px;
    height: 236px;
    background:
      radial-gradient(ellipse 70% 90% at 30% 30%, rgba(111,205,126,0.95) 0%, rgba(111,205,126,0.55) 50%, rgba(39,177,74,0) 100%);
  }
  .tagline {
    position: absolute;
    right: 34px;
    top: 170px;
    font-size: 15.5px;
    font-style: italic;
    line-height: 25px;
    text-align: right;
    color: var(--white);
  }
  .side-label {
    position: absolute;
    font-family: "EB Garamond", Georgia, serif;
    font-style: italic;
    font-size: 15px;
    letter-spacing: 2px;
    color: var(--ink-label);
  }
  .label-front { left: 194px; top: 416px; }
  .label-back { left: 716px; top: 784px; }
</style>
</head>
<body>
<main class="sheet">
  <section class="card card-front">
    <span class="brand-mark"></span>
    <div class="brand-name">Tidal Prime Voltage Collective</div>
    <div class="holder-name">Gus Marwick</div>
    <div class="holder-title">Energy Warrior</div>
    <div class="contact">
      <div class="contact-address">47 Orchard Lane Toronto Ontario K4P 2Z7</div>
      <div class="contact-lines">P (555) 314-2768<span class="contact-sep">•</span>F (555) 862-4091</div>
      <div class="contact-email">gus@tidalprimevoltage.example</div>
    </div>
  </section>
  <p class="side-label label-front">front</p>

  <section class="card card-back">
    <div class="back-art" role="img" aria-label="Illustration: large pale green leaves and lightning bolt sweeping across the card"></div>
    <p class="tagline">Reducing your carbon footprint<br>&amp; energy bill at the same time!</p>
  </section>
  <p class="side-label label-back">back</p>
</main>
</body>
</html>
```